Veltor & Aero Services Business Card Design

a specialised consulting company, aviation specialist, like to have use blue colour on white background.
back of card to have printed-
NDT Expertise:
INSPECTION & TESTING CONSULTING
TRAINING & EDUCATION
CERTIFICATION SERVICES
LEVEL 3 SERVICES
TORVEX / AUDITING
INSPECTION SYSTEMS

Target Market(s)

Mainly the aerospace industry, manufacturers and airframe/engine overhaul companies.

Industry/Entity Type

Business

Contact Information for Business Card

Veltor & Aero Services

Trevor Mulcahy JP

+61 (0)437610582
veltoraeroservices@pindramail.com

Font styles to use
Serif

Colors
3276b4
32a5d5

Requirements
Must have
• aviation style logo with letters VAS part of or adjacent to.

then company name: Veltor & Aero Services

then name in slightly smaller font : Trevor Mulcahy JP

then phone and email details

Back of card, as per brief, but all text to be centred

```html
<!DOCTYPE html>
<html lang="en">
<head>
<meta charset="utf-8">
<title>Veltor &amp; Aero Services – Business Card</title>
<link rel="stylesheet" href="https://fonts.googleapis.com/css2?family=Tinos:wght@400;700&family=Arimo:wght@400&display=swap">
<style>
  :root {
    --brand-blue: #2a77b5;
    --sky-blue: #32a5d5;
    --map-blue: #8cc4ea;
    --wave-blue: #bcdcf3;
    --ink: #111111;
    --paper: #ffffff;
    --stage-light: #d7d8da;
    --stage-dark: #9fa1a4;
  }
  * { margin: 0; padding: 0; box-sizing: border-box; }
  html, body { width: 1200px; height: 1200px; overflow: hidden; }
  body {
    position: relative;
    background: radial-gradient(circle at 50% 45%, var(--stage-light) 0%, #c3c4c6 55%, var(--stage-dark) 100%);
    font-family: "Tinos", "Times New Roman", serif;
  }

  .card {
    position: absolute;
    left: 216px;
    width: 764px;
    height: 461px;
    background: var(--paper);
    overflow: hidden;
  }
  .card--front { top: 131px; }
  .card--back  { top: 600px; }

  /* Front */
  .brand-mark {
    position: absolute;
    left: 410px;
    top: 72px;
    display: flex;
    align-items: center;
    gap: 12px;
    font-family: "Tinos", "Times New Roman", serif;
    font-weight: 700;
    font-size: 56px;
    line-height: 1;
    color: var(--brand-blue);
    transform: translateX(-100%);
  }
  .brand-mark__dot {
    width: 18px; height: 18px;
    border-radius: 50%;
    background: var(--sky-blue);
  }
  .world-map {
    position: absolute;
    left: 378px;
    top: 7px;
    width: 366px;
    height: 222px;
    background: radial-gradient(ellipse at 55% 45%, var(--map-blue) 0%, #b5d9f2 60%, rgba(255,255,255,0) 100%);
    opacity: 0.85;
  }
  .company-name {
    position: absolute;
    left: 0; right: 0;
    top: 225px;
    text-align: center;
    font-weight: 700;
    font-size: 37px;
    letter-spacing: 0.3px;
    color: var(--ink);
  }
  .contact-band {
    position: absolute;
    left: 0; right: 0; bottom: 0;
    height: 165px;
    background: var(--brand-blue);
    color: var(--paper);
  }
  .person-name {
    position: absolute;
    left: 0; right: 0;
    top: 38px;
    text-align: center;
    font-weight: 700;
    font-size: 29px;
  }
  .contact {
    position: absolute;
    top: 114px;
    display: flex;
    align-items: center;
    gap: 8px;
    font-size: 21px;
  }
  .contact--phone { left: 27px; }
  .contact--email { right: 24px; }
  .contact svg { width: 22px; height: 22px; flex: none; }

  /* Back */
  .expertise-title {
    position: absolute;
    left: 0; right: 0;
    top: 32px;
    text-align: center;
    font-weight: 700;
    font-size: 27px;
    color: var(--ink);
  }
  .wave-field {
    position: absolute;
    left: 0; right: 0;
    top: 144px;
    height: 162px;
    background: linear-gradient(170deg, rgba(255,255,255,0) 20%, var(--wave-blue) 55%, rgba(255,255,255,0) 85%);
    opacity: 0.8;
  }
  .expertise-list {
    position: absolute;
    left: 0; right: 0;
    top: 76px;
    list-style: none;
    text-align: center;
    font-family: "Arimo", Arial, sans-serif;
    font-size: 19px;
    line-height: 31px;
    color: var(--ink);
  }
  .back-band {
    position: absolute;
    left: 0; right: 0; bottom: 0;
    height: 155px;
    background: var(--brand-blue);
  }
  .back-band .brand-mark {
    left: 684px;
    top: 58px;
    color: var(--paper);
  }
  .back-band .brand-mark__dot { background: var(--paper); }
</style>
</head>
<body>

  <section class="card card--front">
    <div class="world-map" role="img" aria-label="Dotted world map in light blue"></div>
    <div class="brand-mark"><span class="brand-mark__dot"></span><span>VAS</span></div>
    <h1 class="company-name">VELTOR &amp; AERO SERVICES</h1>

    <div class="contact-band">
      <p class="person-name">Trevor Mulcahy JP</p>
      <p class="contact contact--phone">
        <svg viewBox="0 0 24 24" aria-hidden="true">
          <circle cx="12" cy="12" r="11" fill="#ffffff"/>
          <path d="M8 6.5c-.8.4-1.6 1.5-1.4 2.8.5 3 4 7.2 7.4 8.3 1.2.4 2.4-.2 3-1l-2.2-2.2-1.4 1c-1.6-.8-3.2-2.6-3.8-4.2l1.1-1.3z" fill="#2a77b5"/>
        </svg>
        +61 (0)437610582
      </p>
      <p class="contact contact--email">
        <svg viewBox="0 0 24 24" aria-hidden="true">
          <circle cx="12" cy="12" r="11" fill="#ffffff"/>
          <rect x="5.5" y="7.5" width="13" height="9" fill="none" stroke="#2a77b5" stroke-width="1.5"/>
          <path d="M5.5 7.5 12 13l6.5-5.5" fill="none" stroke="#2a77b5" stroke-width="1.5"/>
        </svg>
        veltoraeroservices@pindramail.com
      </p>
    </div>
  </section>

  <section class="card card--back">
    <div class="wave-field" role="img" aria-label="Flowing light blue line waves"></div>
    <h2 class="expertise-title">NDT Expertise:</h2>
    <ul class="expertise-list">
      <li>INSPECTION &amp; TESTING CONSULTING</li>
      <li>TRAINING &amp; EDUCATION</li>
      <li>CERTIFICATION SERVICES</li>
      <li>LEVEL 3 SERVICES</li>
      <li>TORVEX / AUDITING</li>
      <li>INSPECTION SYSTEMS</li>
    </ul>
    <div class="back-band">
      <div class="brand-mark"><span class="brand-mark__dot"></span><span>VAS</span></div>
    </div>
  </section>

</body>
</html>
```